Business card website / business card for website

We are a French website selling products Made in USA of quality, we need a business card to give from hand to hand and for deposit in the cartons of Each order. We-have the logo That I send in the attachments The theme is: US Vintage and find the compromised entre les national park ambience us and the atmosphere Brooklyn If you can make the feeling it's great The site www.latablederivebleue.com (opening April) You can change the logo a little gold in color it could ... we are a French website selling products Made in USA quality, we need a business card to give from hand to hand and deposit in cartons each order. we have the logo that I convey in the attached parts is the theme: Vintage embiance US and find a compromise between the atmosphere us national park and the atmosphere Brooklyn at: www.latablederivebleue.com (opening April) if you can the impression is great

Target Market(s)

25-50 YEARS man, woman.

Industry/Entity Type

Business

Contact Information for Business Card

www.latablederivebleue.com
N'oubliez pas que nous sommes là si vous avez besoin de nouscontact@latablederivebleue.com

Font styles to use
Serif

Requirements
Must have
• my logo with "general store", my email address preceded by the phrase: Do not forget that we are here if you need us My logo with the words "general store," my email address Preceded by the sentence: remember we're here if you need us (in french)
Nice to have
• i like this style: http://designcorbel.net/ideas/print-ideas/25-charming-old-style-business-card-designs/ must feel the Vintage America it must feel the Vintage America lice can change a little logo or to color ... You can change the logo a little gold in color it could ... i like kraft paper with red ....
Should not have

```html
<!DOCTYPE html>
<html lang="fr">
<head>
<meta charset="utf-8">
<title>La Table de Rive Bleue — Cartes de visite</title>
<link rel="stylesheet" href="https://fonts.googleapis.com/css2?family=PT+Sans:wght@400;700&display=swap">
<style>
  :root {
    --backdrop: #d9d9d9;
    --card-dark: #3b3b3b;
    --card-dark-light: #4a4a4a;
    --card-light: #ffffff;
    --ink-light: #ffffff;
    --ink-dark: #2e2e2e;
    --rule: #bdbdbd;
    --mark-tone: #8c8c8c;
  }
  html, body {
    margin: 0;
    width: 1200px;
    height: 900px;
    overflow: hidden;
    background: var(--backdrop);
  }
  .canvas {
    position: relative;
    width: 1200px;
    height: 900px;
    font-family: "PT Sans", sans-serif;
  }
  .card {
    position: absolute;
    top: 185px;
    width: 302px;
    height: 489px;
    border-radius: 12px;
    overflow: hidden;
    background: var(--card-dark);
  }
  .card--front { left: 299px; }
  .card--back {
    left: 646px;
    width: 303px;
    background: radial-gradient(circle at 50% 50%, var(--card-dark-light) 0%, var(--card-dark) 70%);
  }
  .card__arc {
    position: absolute;
    inset: 0;
  }
  .brand-mark {
    position: absolute;
    width: 184px;
    height: 184px;
    border-radius: 50%;
    display: flex;
    align-items: center;
    justify-content: center;
    text-align: center;
    box-sizing: border-box;
    padding: 24px;
  }
  .brand-mark__scene {
    position: absolute;
    inset: 10px;
    border-radius: 50%;
    opacity: .35;
  }
  .brand-mark__name {
    position: relative;
    font-size: 20px;
    font-weight: 700;
    line-height: 1.15;
    letter-spacing: .5px;
    text-transform: uppercase;
  }
  .card--front .brand-mark {
    left: 59px;
    top: 23px;
    border: 2px solid var(--ink-dark);
  }
  .card--front .brand-mark__scene { background: radial-gradient(circle, #cfcfcf, #ffffff); }
  .card--front .brand-mark__name { color: var(--ink-dark); }
  .card--back .brand-mark {
    left: 60px;
    top: 156px;
    border: 2px solid var(--ink-light);
  }
  .card--back .brand-mark__scene { background: radial-gradient(circle, #9a9a9a, var(--card-dark)); }
  .card--back .brand-mark__name { color: var(--ink-light); }
  .front__content {
    position: absolute;
    left: 0;
    right: 0;
    top: 322px;
    text-align: center;
    color: var(--ink-light);
  }
  .front__title {
    margin: 0;
    font-size: 22px;
    font-weight: 700;
    letter-spacing: .3px;
  }
  .front__rule {
    width: 121px;
    height: 1px;
    margin: 13px auto 14px;
    border: 0;
    background: var(--rule);
  }
  .front__message {
    margin: 0;
    font-size: 13.5px;
    line-height: 17px;
  }
  .back__url {
    position: absolute;
    left: 0;
    right: 0;
    top: 417px;
    margin: 0;
    text-align: center;
    font-size: 13.5px;
    color: var(--ink-light);
  }
</style>
</head>
<body>
  <main class="canvas">
    <section class="card card--front">
      <svg class="card__arc" width="302" height="489" viewBox="0 0 302 489" aria-hidden="true">
        <rect x="0" y="0" width="302" height="80" fill="var(--card-light)"/>
        <circle cx="151" cy="75" r="176" fill="var(--card-light)"/>
        <circle cx="151" cy="75" r="168" fill="none" stroke="var(--ink-dark)" stroke-width="2"/>
      </svg>
      <div class="brand-mark">
        <div class="brand-mark__scene" role="img" aria-label="Illustration of a wooden barn among pine trees"></div>
        <span class="brand-mark__name">La Table de Rive Bleue</span>
      </div>
      <div class="front__content">
        <h1 class="front__title">GENERAL STORE</h1>
        <hr class="front__rule">
        <p class="front__message">N'oubliez pas que nous sommes<br>là si vous avez besoin de<br>nouscontact@latablederivebleue.com</p>
      </div>
    </section>

    <section class="card card--back">
      <div class="brand-mark">
        <div class="brand-mark__scene" role="img" aria-label="Illustration of a wooden barn among pine trees"></div>
        <span class="brand-mark__name">La Table de Rive Bleue</span>
      </div>
      <p class="back__url">www.latablederivebleue.com</p>
    </section>
  </main>
</body>
</html>
```